Accounting Practice Business Card Design

I have a logo I am happy for you to use in the design of the Business Card.
You can edit and change colours as you please, I am not fixated on it.
I am looking for a modern and clean overall feel for the finished design.

The business is a small accounting practice who thrives on word of mouth referrals and this card will be given to all current and prospect clients.

Industry/Entity Type

Accountant

Contact Information for Business Card

Marcus Elwin
Level 5, 8 Corvale Ridge Road
ASHGROVE RISE VIC 3187
Phone: 9481 3057
Email: melwin@mrfaccountants.com.au
Web: www.mrfaccountants.com.au

Font styles to use
Serif
Sans Serif

Colors
0555a3
3277b5
85acd3
0393ce
33a6d7
85cae6
00a990
33b8a4
9bcb3c

Requirements
Must have
• "The end to your tax problems begin with us"
• "A referral from you is our greatest compliment"
Nice to have
• Modern clean professional

```html
<!DOCTYPE html>
<html lang="en">
<head>
<meta charset="utf-8">
<title>MRF Accountants – Business Card</title>
<link href="https://fonts.googleapis.com/css2?family=Montserrat:wght@400;500;600;700&display=swap" rel="stylesheet">
<style>
  :root {
    --backdrop: #3d3935;
    --brand-green: #2f7a35;
    --brand-blue: #0f4e93;
    --card-white: #ffffff;
    --ink-dark: #333333;
    --ink-grey: #555555;
    --link-green: #2f7a35;
  }
  * { margin: 0; padding: 0; box-sizing: border-box; }
  html, body {
    width: 1200px; height: 930px; overflow: hidden;
    background: var(--backdrop);
    font-family: "Montserrat", Arial, sans-serif;
  }
  .card {
    position: absolute;
    left: 265px;
    width: 670px; height: 383px;
    border-radius: 18px;
    overflow: hidden;
  }
  /* Back side */
  .card--back {
    top: 50px;
    background: var(--brand-green);
    color: #fff;
    text-align: center;
  }
  .card--back .wordmark {
    margin-top: 92px;
    font-size: 44px; font-weight: 700; letter-spacing: 2px;
  }
  .card--back .referral {
    margin-top: 30px;
    font-size: 19px; font-weight: 400; line-height: 1.55; letter-spacing: 0.6px;
  }
  .card--back .signoff {
    margin-top: 16px;
    font-size: 13px; font-weight: 600; letter-spacing: 0.5px;
  }
  /* Front side */
  .card--front {
    top: 497px;
    background: var(--card-white);
  }
  .edge-stripe { position: absolute; left: 0; top: 0; width: 24px; height: 383px; }
  .front-header { position: absolute; left: 58px; top: 52px; }
  .front-header .company {
    color: var(--brand-green); font-size: 23px; font-weight: 500; letter-spacing: 0.5px;
  }
  .front-header .tagline {
    color: var(--ink-dark); font-size: 14.5px; font-weight: 600; margin-top: 2px;
  }
  .holder { position: absolute; left: 92px; top: 140px; }
  .holder .name {
    color: var(--brand-blue); font-size: 32px; font-weight: 600; letter-spacing: 0.5px;
  }
  .holder .role { color: var(--ink-grey); font-size: 15px; }
  .address {
    position: absolute; left: 118px; top: 222px;
    font-style: normal;
    color: var(--ink-grey); font-size: 15px; line-height: 1.35; letter-spacing: 0.4px;
  }
  .contact-list {
    position: absolute; left: 100px; top: 285px;
    list-style: none; color: var(--ink-grey); font-size: 15px; line-height: 1.45; letter-spacing: 0.3px;
  }
  .contact-list li { display: flex; align-items: center; gap: 10px; }
  .contact-list svg { width: 13px; height: 13px; flex: none; }
  .contact-list .web-domain { color: var(--link-green); }
  .front-wordmark {
    position: absolute; right: 40px; top: 105px;
    width: 250px;
    display: flex; align-items: center; gap: 12px;
    color: var(--brand-blue); font-size: 28px; font-weight: 700; letter-spacing: 1px;
    line-height: 1.15;
  }
  .front-wordmark .mark-dot {
    width: 20px; height: 20px; border-radius: 50%; background: var(--brand-green); flex: none;
  }
</style>
</head>
<body>
  <section class="card card--back">
    <div class="wordmark">MRF ACCOUNTANTS</div>
    <p class="referral">A referral from you is our<br>greatest compliment.<br>Thank you for choosing us.</p>
    <p class="signoff">MRF ACCOUNTANTS</p>
  </section>

  <section class="card card--front">
    <svg class="edge-stripe" viewBox="0 0 24 383" aria-hidden="true">
      <polygon points="0,0 24,0 24,235 0,260" fill="var(--brand-green)"/>
      <polygon points="0,260 24,235 24,383 0,383" fill="var(--brand-blue)"/>
    </svg>

    <header class="front-header">
      <div class="company">MRF ACCOUNTANTS</div>
      <div class="tagline">The end to your tax problems begin with us.</div>
    </header>

    <div class="holder">
      <div class="name">MARCUS ELWIN</div>
      <div class="role">Accountant</div>
    </div>

    <address class="address">
      Level 5, 8 Corvale Ridge Road<br>ASHGROVE RISE VIC 3187
    </address>

    <ul class="contact-list">
      <li>
        <svg viewBox="0 0 16 16"><path d="M4 1l3 3-2 2c1 2 3 4 5 5l2-2 3 3-2 3C7 14 2 9 1 3z" fill="var(--brand-blue)"/></svg>
        9481 3057
      </li>
      <li>
        <svg viewBox="0 0 16 16"><rect x="1" y="3" width="14" height="10" fill="none" stroke="var(--brand-blue)" stroke-width="1.6"/><path d="M1 3l7 6 7-6" fill="none" stroke="var(--brand-blue)" stroke-width="1.6"/></svg>
        melwin@mrfaccountants.com.au
      </li>
      <li>
        <svg viewBox="0 0 16 16"><circle cx="8" cy="8" r="6.5" fill="none" stroke="var(--brand-blue)" stroke-width="1.4"/><path d="M1.5 8h13M8 1.5c-3 3-3 10 0 13M8 1.5c3 3 3 10 0 13" fill="none" stroke="var(--brand-blue)" stroke-width="1.2"/></svg>
        <span>www.<span class="web-domain">mrfaccountants.com.au</span></span>
      </li>
    </ul>

    <div class="front-wordmark">
      <span class="mark-dot"></span>
      <span>MRF<br>ACCOUNTANTS</span>
    </div>
  </section>
</body>
</html>
```